Design a Website for an IT Support Company

We are an IT support company that provides commercial IT support and services to small and medium sized businesses. We are in need of a website to be developed for our business.
We would like to work with someone who is either familiar with the IT field, or has developed a website for an IT support company in the past.
Some examples of designs/layouts that we like:
https://www.veltragrid.example/
http://www.morvashelp.example/
http://kelbo.example/
http://www.nuvopathsystems.example/
http://www.quordesk.example/
I have attached a word document that gives a menu system/page layout format that we would like for our website as well as branch office phone numbers. Our logo is also attached that you can use for your design purposes. We currently do not have copy produced for all of the pages outlined in the word document, but would get this done during the project with the selected designer.
We would like the website to be SEO friendly & fully responsive. We would prefer a Wordpress format, however, we are open to HTML formats as well.

```html
<!DOCTYPE html>
<html lang="en">
<head>
<meta charset="utf-8">
<title>Corvan IT – IT Support for Small and Medium Businesses</title>
<link rel="stylesheet" href="https://fonts.googleapis.com/css2?family=Open+Sans:wght@400;600;700;800&display=swap">
<style>
:root{
  --blue:#1b73c2;
  --blue-dark:#155f9f;
  --ink:#2b2b2b;
  --dark:#2a2a2a;
  --darker:#1d1d1d;
  --green:#3ea52c;
  --grey-bg:#f1f1f1;
  --card:#f6f6f6;
  --muted:#666;
  --white:#fff;
}
*{box-sizing:border-box;margin:0;padding:0}
html,body{width:1200px;height:3673px;overflow:hidden}
body{font-family:'Open Sans',Arial,sans-serif;color:var(--ink);background:var(--white);position:relative}
.wrap{width:1054px;margin:0 auto;position:relative}
section,header,footer{position:relative;width:1200px}

/* header */
.site-header{height:122px}
.brand{position:absolute;left:76px;top:18px;display:flex;align-items:center;gap:12px}
.brand-dot{width:54px;height:54px;border-radius:50%;background:var(--blue)}
.brand-name{font-size:40px;font-weight:700;color:var(--ink);letter-spacing:-.5px}
.cta-top{position:absolute;left:510px;top:18px;height:40px;width:392px;border:2px solid var(--green);color:var(--green);font-size:13px;font-weight:700;display:flex;align-items:center;justify-content:center}
.phone-top{position:absolute;left:926px;top:20px;display:flex;align-items:center;gap:12px;font-size:25px;font-weight:700;color:var(--blue)}
.phone-top .ico{width:32px;height:32px;border-radius:50%;background:#777;display:flex;align-items:center;justify-content:center}
.main-nav{position:absolute;right:73px;top:84px;display:flex;gap:0}
.main-nav a{font-size:14px;font-weight:700;color:var(--ink);text-decoration:none;padding:0 0 0 56px}
.main-nav a.active{color:var(--blue)}

/* hero */
.hero{height:556px;background:linear-gradient(100deg,#c9d2dc 0%,#aeb9c5 35%,#dfe3e7 60%,#f1ede9 100%)}
.hero-caption{position:absolute;left:73px;top:196px;width:539px;height:160px;background:rgba(20,20,20,.85);padding:14px 22px;color:var(--white)}
.hero-caption h1{font-size:38px;font-weight:800;line-height:1.1;letter-spacing:.5px}
.hero-caption h1 span{color:#3d9be9}
.hero-caption p{font-size:20px;font-weight:700;line-height:1.4;margin-top:8px}
.dots{position:absolute;display:flex;gap:8px}
.dots i{width:12px;height:12px;border-radius:50%;background:#fff;opacity:.7}
.dots i.on{opacity:1;background:var(--blue)}
.hero .dots{left:575px;bottom:22px}

/* services */
.services{height:490px}
.section-title{font-size:25px;font-weight:700;text-align:center;letter-spacing:.5px}
.services .section-title{padding-top:46px}
.service-cards{position:absolute;top:101px;left:76px;display:flex;gap:30px}
.service-card{width:330px;height:335px;background:var(--card);box-shadow:0 4px 10px rgba(0,0,0,.12);padding:30px 24px 0}
.service-head{display:flex;align-items:center;gap:26px;margin-bottom:24px}
.service-head h3{font-size:22px;font-weight:700;color:var(--blue)}
.service-card ul{list-style:none}
.service-card li{font-size:15px;color:#444;line-height:29.5px;display:flex;align-items:center;gap:14px}
.service-card li svg{flex:none}
.btn-blue{display:inline-block;background:var(--blue);color:var(--white);font-weight:700;font-size:12px;padding:9px 14px;margin-top:18px;text-decoration:none}

/* welcome */
.welcome{height:362px;background:var(--dark);display:flex}
.welcome-photo{width:580px;height:362px;background:linear-gradient(120deg,#dfe4ea,#9aa6b2 60%,#707c88);clip-path:polygon(0 0,100% 0,91% 100%,0 100%)}
.welcome-text{position:absolute;left:640px;top:64px;width:480px;color:var(--white)}
.welcome-text h2{font-size:24px;font-weight:700;margin-bottom:18px}
.welcome-text p{font-size:14px;line-height:1.9;color:#e2e2e2}
.welcome-text .btn-blue{font-size:14px;padding:15px 33px;margin-top:26px}

/* why */
.why{height:821px;background:var(--blue);color:var(--white)}
.why .section-title{padding-top:54px;color:var(--white)}
.video-frame{position:absolute;left:287px;top:106px;width:624px;height:367px;border:6px solid #3f92d8;background:linear-gradient(135deg,#4e6c86,#9eb2c4 50%,#4f6577)}
.play{position:absolute;left:50%;top:50%;width:64px;height:64px;margin:-32px 0 0 -32px;border-radius:50%;background:rgba(255,255,255,.9);display:flex;align-items:center;justify-content:center}
.features{position:absolute;top:548px;left:73px;width:1054px;display:flex}
.feature{flex:1;text-align:center;padding:0 50px;border-right:1px solid rgba(255,255,255,.2)}
.feature:last-child{border-right:0}
.feature .circle{width:84px;height:84px;border-radius:50%;background:var(--ink);border:4px solid var(--white);margin:0 auto 22px;display:flex;align-items:center;justify-content:center}
.feature h4{font-size:17px;font-weight:700;line-height:1.3;margin-bottom:8px}
.feature p{font-size:14.5px;line-height:1.5;color:#eaf2fa}
.arrow{position:absolute;top:640px}
.arrow.left{left:44px}.arrow.right{right:44px}

/* testimonials */
.testimonials{height:441px}
.testimonials .section-title{padding-top:38px}
.quotes{position:absolute;top:98px;left:76px;display:flex;gap:30px}
.quote{width:330px;text-align:center;position:relative}
.quote-box{background:var(--grey-bg);height:196px;padding:22px 28px 0;position:relative}
.quote-box p{font-size:14px;font-style:italic;line-height:1.55;color:#555}
.quote-name{font-size:13px;font-weight:700;color:var(--blue);margin-top:12px}
.qmark{position:absolute;font-size:90px;font-weight:800;color:#d9d9d9;line-height:1;font-family:Georgia,serif}
.qmark.open{left:10px;top:-4px}.qmark.close{right:16px;bottom:-30px}
.avatar{width:74px;height:74px;border-radius:50%;margin:-38px auto 0;border:3px solid var(--white);background:linear-gradient(#c8c8c8,#8b8b8b);position:relative}
.testimonials .dots{left:573px;top:366px}
.testimonials .dots i{background:#444;opacity:1}
.testimonials .dots i.on{background:var(--blue)}

/* partners */
.partners{height:196px;background:var(--grey-bg)}
.partners .section-title{padding-top:34px}
.partner-row{position:absolute;top:100px;left:76px;width:1048px;display:flex;justify-content:space-between;align-items:center}
.partner-badge{height:52px;background:#c9ced4;border-radius:4px}

/* schedule */
.schedule{height:338px;background:var(--dark);color:var(--white)}
.schedule .section-title{padding-top:52px;color:var(--white);font-size:26px}
.form-grid{position:absolute;left:255px;top:114px;width:693px;display:grid;grid-template-columns:333px 333px;gap:13px 27px}
.field{height:42px;background:var(--white);color:#444;font-size:14px;padding:0 12px;display:flex;align-items:center}
.btn-green{position:absolute;left:497px;top:236px;width:208px;height:50px;background:var(--green);color:var(--white);font-size:15px;font-weight:700;display:flex;align-items:center;justify-content:center}

/* footer */
.site-footer{height:286px;background:var(--blue);color:var(--white)}
.foot-brand{position:absolute;left:76px;top:52px;display:flex;align-items:center;gap:10px}
.foot-brand .brand-dot{width:44px;height:44px;background:var(--white)}
.foot-brand span{font-size:32px;font-weight:700}
.branches{position:absolute;left:76px;top:132px;font-size:12.5px;line-height:22px;display:grid;grid-template-columns:132px auto}
.foot-col{position:absolute;top:52px}
.foot-col h5{font-size:12.5px;font-weight:700;margin-bottom:14px}
.foot-col.sitemap{left:368px}
.foot-col.sitemap a{display:block;font-size:12.5px;color:var(--white);text-decoration:none;line-height:31px}
.foot-col.blog{left:534px}
.post{display:flex;gap:22px;margin-bottom:20px}
.post-thumb{width:78px;height:54px;background:linear-gradient(135deg,#dfe7ef,#9fb3c6)}
.post b{display:block;font-size:13px;font-weight:700}
.post span{font-size:12.5px;line-height:1.5;color:#e3eefa}
.foot-col.signup{left:885px}
.email-input{width:242px;height:40px;background:var(--white);color:#777;font-size:13px;padding:0 12px;display:flex;align-items:center}
.btn-dark{margin:14px 0 0 150px;width:92px;height:42px;background:var(--darker);font-size:13px;font-weight:700;display:flex;align-items:center;justify-content:center}
.bottom-bar{height:61px;background:var(--darker);color:#999;font-size:11px;display:flex;align-items:center;padding:0 76px;justify-content:space-between}
.social{display:flex;gap:16px}
.social i{width:18px;height:18px;border-radius:50%;background:#ddd;display:block}
</style>
</head>
<body>

<header class="site-header">
  <div class="brand"><span class="brand-dot"></span><span class="brand-name">Corvan IT</span></div>
  <div class="cta-top">SCHEDULE A FREE NETWORK ASSESSMENT TODAY!</div>
  <div class="phone-top">
    <span class="ico"><svg width="18" height="18" viewBox="0 0 24 24"><path fill="#fff" d="M6.6 10.8a15 15 0 0 0 6.6 6.6l2.2-2.2a1 1 0 0 1 1-.25 11.4 11.4 0 0 0 3.6.57 1 1 0 0 1 1 1V20a1 1 0 0 1-1 1A17 17 0 0 1 3 4a1 1 0 0 1 1-1h3.5a1 1 0 0 1 1 1c0 1.25.2 2.45.57 3.57a1 1 0 0 1-.25 1z"/></svg></span>
    555-010-2200
  </div>
  <nav class="main-nav">
    <a class="active" href="#">HOME</a><a href="#">DATA</a><a href="#">CLOUD</a><a href="#">VOICE</a><a href="#">CONTACT</a>
  </nav>
</header>

<section class="hero" role="img" aria-label="Helpdesk agent wearing a headset in a busy support office">
  <div class="hero-caption">
    <h1>HELPDESK <span>SUPPORT</span></h1>
    <p>We are an IT support company that provides commercial IT support and services to small and medium sized businesse.</p>
  </div>
  <div class="dots"><i></i><i class="on"></i><i></i></div>
</section>

<section class="services">
  <h2 class="section-title">OUR SERVICES</h2>
  <div class="service-cards">
    <article class="service-card">
      <div class="service-head">
        <svg width="52" height="58" viewBox="0 0 52 58"><g fill="#333"><ellipse cx="26" cy="9" rx="24" ry="8"/><path d="M2 14c0 5 11 8 24 8s24-3 24-8v10c0 5-11 8-24 8S2 29 2 24z"/><path d="M2 30c0 5 11 8 24 8s24-3 24-8v10c0 5-11 8-24 8S2 45 2 40z"/></g></svg>
        <h3>DATA</h3>
      </div>
      <ul>
        <li><svg width="14" height="12" viewBox="0 0 14 12"><path d="M1 6l4 4 8-9" stroke="#1b73c2" stroke-width="2.5" fill="none"/></svg>Managed IT Services</li>
        <li><svg width="14" height="12" viewBox="0 0 14 12"><path d="M1 6l4 4 8-9" stroke="#1b73c2" stroke-width="2.5" fill="none"/></svg>IT Support &amp; Consulting</li>
        <li><svg width="14" height="12" viewBox="0 0 14 12"><path d="M1 6l4 4 8-9" stroke="#1b73c2" stroke-width="2.5" fill="none"/></svg>IT Helpdesk Services</li>
        <li><svg width="14" height="12" viewBox="0 0 14 12"><path d="M1 6l4 4 8-9" stroke="#1b73c2" stroke-width="2.5" fill="none"/></svg>Network Security</li>
        <li><svg width="14" height="12" viewBox="0 0 14 12"><path d="M1 6l4 4 8-9" stroke="#1b73c2" stroke-width="2.5" fill="none"/></svg>Data Backup &amp; Recovery</li>
      </ul>
      <a class="btn-blue" href="#">READ MORE</a>
    </article>
    <article class="service-card">
      <div class="service-head">
        <svg width="62" height="44" viewBox="0 0 62 44"><path fill="#333" d="M50 18a17 17 0 0 0-32-6 12 12 0 0 0-5 23h37a12 12 0 0 0 0-17z"/></svg>
        <h3>CLOUD</h3>
      </div>
      <ul>
        <li><svg width="14" height="12" viewBox="0 0 14 12"><path d="M1 6l4 4 8-9" stroke="#1b73c2" stroke-width="2.5" fill="none"/></svg>Workdesk Suite Migrations</li>
        <li><svg width="14" height="12" viewBox="0 0 14 12"><path d="M1 6l4 4 8-9" stroke="#1b73c2" stroke-width="2.5" fill="none"/></svg>Skyrack Management Services</li>
        <li><svg width="14" height="12" viewBox="0 0 14 12"><path d="M1 6l4 4 8-9" stroke="#1b73c2" stroke-width="2.5" fill="none"/></svg>Cloud Migration Services</li>
        <li><svg width="14" height="12" viewBox="0 0 14 12"><path d="M1 6l4 4 8-9" stroke="#1b73c2" stroke-width="2.5" fill="none"/></svg>Hosted Virtual Servers</li>
        <li><svg width="14" height="12" viewBox="0 0 14 12"><path d="M1 6l4 4 8-9" stroke="#1b73c2" stroke-width="2.5" fill="none"/></svg>Hosted Telephone Systems</li>
      </ul>
      <a class="btn-blue" href="#">READ MORE</a>
    </article>
    <article class="service-card">
      <div class="service-head">
        <svg width="50" height="50" viewBox="0 0 24 24"><path fill="#333" d="M6.6 10.8a15 15 0 0 0 6.6 6.6l2.2-2.2a1 1 0 0 1 1-.25 11.4 11.4 0 0 0 3.6.57 1 1 0 0 1 1 1V20a1 1 0 0 1-1 1A17 17 0 0 1 3 4a1 1 0 0 1 1-1h3.5a1 1 0 0 1 1 1c0 1.25.2 2.45.57 3.57a1 1 0 0 1-.25 1z"/></svg>
        <h3>VOICE</h3>
      </div>
      <ul>
        <li><svg width="14" height="12" viewBox="0 0 14 12"><path d="M1 6l4 4 8-9" stroke="#1b73c2" stroke-width="2.5" fill="none"/></svg>Starline Consulting</li>
        <li><svg width="14" height="12" viewBox="0 0 14 12"><path d="M1 6l4 4 8-9" stroke="#1b73c2" stroke-width="2.5" fill="none"/></svg>Business Telephone Systems</li>
        <li><svg width="14" height="12" viewBox="0 0 14 12"><path d="M1 6l4 4 8-9" stroke="#1b73c2" stroke-width="2.5" fill="none"/></svg>Multiple Office Phone Systems</li>
        <li><svg width="14" height="12" viewBox="0 0 14 12"><path d="M1 6l4 4 8-9" stroke="#1b73c2" stroke-width="2.5" fill="none"/></svg>Tonewave Telephone Systems</li>
        <li><svg width="14" height="12" viewBox="0 0 14 12"><path d="M1 6l4 4 8-9" stroke="#1b73c2" stroke-width="2.5" fill="none"/></svg>SIP Trunks</li>
      </ul>
      <a class="btn-blue" href="#">READ MORE</a>
    </article>
  </div>
</section>

<section class="welcome">
  <div class="welcome-photo" role="img" aria-label="Support team working at computers with headsets"></div>
  <div class="welcome-text">
    <h2>WELCOME TO OUR WEBSITE</h2>
    <p>Technology is the backbone of your business. Corvan IT excels at providing outsourced network IT support to businesses just like yours. Our team of friendly and highly experienced engineers are standing by to help you get the most out of your technology.</p>
    <a class="btn-blue" href="#">READ MORE</a>
  </div>
</section>

<section class="why">
  <h2 class="section-title">WHY CORVAN IT</h2>
  <div class="video-frame" role="img" aria-label="Intro video still: hands holding a tablet showing a support agent">
    <div class="play"><svg width="26" height="28" viewBox="0 0 26 28"><path d="M4 2l20 12L4 26z" fill="#333"/></svg></div>
  </div>
  <svg class="arrow left" width="16" height="26" viewBox="0 0 16 26"><path d="M13 2L3 13l10 11" stroke="#fff" stroke-width="3" fill="none"/></svg>
  <svg class="arrow right" width="16" height="26" viewBox="0 0 16 26"><path d="M3 2l10 11L3 24" stroke="#fff" stroke-width="3" fill="none"/></svg>
  <div class="features">
    <div class="feature">
      <div class="circle"><svg width="34" height="34" viewBox="0 0 24 24"><circle cx="9" cy="9" r="5" stroke="#fff" stroke-width="2.4" fill="none"/><circle cx="17" cy="17" r="3.5" stroke="#fff" stroke-width="2.2" fill="none"/></svg></div>
      <h4>Control IT Spending</h4>
      <p>We offer an all-inclusive proactive, reliable, and affordable solution for your IT support needs..</p>
    </div>
    <div class="feature">
      <div class="circle"><svg width="34" height="34" viewBox="0 0 24 24"><path d="M3 3v18h18" stroke="#fff" stroke-width="2" fill="none"/><path d="M6 16l4-5 3 3 6-7" stroke="#fff" stroke-width="2.2" fill="none"/></svg></div>
      <h4>Optimized IT Efficiency</h4>
      <p>Technology is not a one size fits all approach. Corvan IT determines and implements solutions...</p>
    </div>
    <div class="feature">
      <div class="circle"><svg width="34" height="34" viewBox="0 0 24 24"><g fill="#fff"><rect x="9" y="2" width="6" height="6"/><rect x="2" y="16" width="6" height="6"/><rect x="9" y="16" width="6" height="6"/><rect x="16" y="16" width="6" height="6"/></g><path d="M12 8v8M5 16v-4h14v4" stroke="#fff" stroke-width="1.6" fill="none"/></svg></div>
      <h4>Real Proactive Network Management</h4>
      <p>Our approach to IT support and network management is based upon a proven checklist...</p>
    </div>
  </div>
</section>

<section class="testimonials">
  <h2 class="section-title">CUSTOMER TESTIMONIALS</h2>
  <div class="quotes">
    <div class="quote">
      <div class="quote-box"><span class="qmark open">“</span><span class="qmark close">”</span>
        <p>Aliquam molestie, mi et imperdiet euismod, dui purus auctor tellus, et interdum lacus lectus et ante. Sed accumsan sollicitudin sapien, sit amet adipiscing turpis...</p>
        <div class="quote-name">-NAME HEADING</div></div>
      <div class="avatar" role="img" aria-label="Customer portrait"></div>
    </div>
    <div class="quote">
      <div class="quote-box"><span class="qmark open">“</span><span class="qmark close">”</span>
        <p>Aliquam molestie, mi et imperdiet euismod, dui purus auctor tellus, et interdum lacus lectus et ante. Sed accumsan sollicitudin sapien, sit amet adipiscing turpis...</p>
        <div class="quote-name">-NAME HEADING</div></div>
      <div class="avatar" role="img" aria-label="Customer portrait"></div>
    </div>
    <div class="quote">
      <div class="quote-box"><span class="qmark open">“</span><span class="qmark close">”</span>
        <p>Aliquam molestie, mi et imperdiet euismod, dui purus auctor tellus, et interdum lacus lectus et ante. Sed accumsan sollicitudin sapien, sit amet adipiscing turpis...</p>
        <div class="quote-name">-NAME HEADING</div></div>
      <div class="avatar" role="img" aria-label="Customer portrait"></div>
    </div>
  </div>
  <div class="dots"><i class="on"></i><i></i><i></i></div>
</section>

<section class="partners">
  <h2 class="section-title">OUR PARTNERS</h2>
  <div class="partner-row">
    <div class="partner-badge" style="width:92px"></div>
    <div class="partner-badge" style="width:140px"></div>
    <div class="partner-badge" style="width:110px"></div>
    <div class="partner-badge" style="width:226px"></div>
    <div class="partner-badge" style="width:178px"></div>
    <div class="partner-badge" style="width:96px"></div>
  </div>
</section>

<section class="schedule">
  <h2 class="section-title">SCHEDULE A FREE NETWORK ASSESSMENT TODAY</h2>
  <div class="form-grid">
    <div class="field">Name</div><div class="field">Company Name</div>
    <div class="field">Email Address</div><div class="field">Phone No.</div>
  </div>
  <div class="btn-green">SCHEDULE NOW</div>
</section>

<footer class="site-footer">
  <div class="foot-brand"><span class="brand-dot"></span><span>Corvan IT</span></div>
  <div class="branches">
    <span>Main Number:</span><span>555-010-2200</span>
    <span>Houston:</span><span>555-010-3100</span>
    <span>San Antonio:</span><span>555-010-4200</span>
    <span>Austin:</span><span>555-010-5300</span>
    <span>Tulsa:</span><span>555-010-6400</span>
    <span>Oklahoma City:</span><span>555-010-7500</span>
  </div>
  <div class="foot-col sitemap">
    <h5>SITE MAP</h5>
    <a href="#">Home</a><a href="#">Services</a><a href="#">Why Corvan IT</a><a href="#">Contact us</a>
  </div>
  <div class="foot-col blog">
    <h5>BLOG POSTS</h5>
    <div class="post"><div class="post-thumb" role="img" aria-label="Blog post thumbnail"></div><div><b>Consectetuer adipiscing elit</b><span>Aenean a nibh eget turpis<br>vehicula tempus ac...</span></div></div>
    <div class="post"><div class="post-thumb" role="img" aria-label="Blog post thumbnail"></div><div><b>Consectetuer adipiscing elit</b><span>Aenean a nibh eget turpis<br>vehicula tempus ac...</span></div></div>
  </div>
  <div class="foot-col signup">
    <h5>EMAIL SIGN UP</h5>
    <div class="email-input">Enter Email Address</div>
    <div class="btn-dark">SIGN UP</div>
  </div>
</footer>
<div class="bottom-bar">
  <span>Copyright © 2017. Company Name. All Right Reserved</span>
  <div class="social"><i></i><i></i><i></i><i></i><i></i><i></i></div>
</div>

</body>
</html>
```